Educational Institution needs a new website

A little bit about ourselves:
Brimley College is a multicultural K-12 school with students who represent nearly 30 ethnic and cultural backgrounds. It is one of the fastest growing schools in the City of Canning (in Perth, Western Australia), and offers quality education with a unique school environment at two campuses.
The mission of Brimley College is to equip students with moral values, academic knowledge and 21st century skills. We empower students to unlock their potential to be confident global citizens.
Brimley College strives to educate students in a manner which inspires them to become lifelong learners. We are committed to raising individuals who are tolerant and respectful towards others enabling them to grow into citizens who contribute to the common good of society.
Here are our design goals:
#1: To emphasise the growth of the school from a small school community to a much larger prestigious college.
#2: Have current and prospective parents have a clear understanding of our college’s morals and values and how we differ from other colleges.
#3: Highlight that our school provides a joyful and safe environment, which is highly valued by parents.
#4: Emphasise that our school presents a welcoming atmosphere for parents as we have strong relationships with our community.
#5: Highlight the various after-school activities available to our students, which are provided through the clubs and pastoral care department.
#6: Allow for online registrations and the option of adding student, staff and parent portals.
#7: Follow the existing school colours
We would like to request the design for the home page and a secondary page to see the alternative layouts.
Other information:
Please note that our logo is will be changed slightly in the upcoming weeks. Please keep this in mind while designing.
We will have another contest for the coding of the website.
We want to be able to make amendments and additions to the content of the website in the future and would like to make sure we have a strong communication with the designer.
The existing website is https://www.brimley-example.edu.au/ for reference for school colours and content.
Education

```html
<!DOCTYPE html>
<html lang="en">
<head>
<meta charset="utf-8">
<title>Brimley College</title>
<link href="https://fonts.googleapis.com/css2?family=Poppins:wght@400;500;600&display=swap" rel="stylesheet">
<style>
:root{
  --blue-dark:#1a66a3;
  --blue:#29a8e0;
  --blue-mid:#1f6fae;
  --ink:#222;
  --grey-text:#777;
  --panel:#f5f5f5;
  --band:#ebebeb;
  --white:#fff;
}
*{box-sizing:border-box;margin:0;padding:0}
html,body{width:1200px;height:3115px;overflow:hidden;background:var(--white);font-family:'Poppins',sans-serif;color:var(--ink)}
.page{position:relative;width:1200px;height:3115px}
.abs{position:absolute}

/* header */
.brand{left:85px;top:38px;display:flex;align-items:center;gap:12px;font-weight:600;font-size:27px;color:var(--blue-dark);letter-spacing:.5px}
.brand-dot{width:26px;height:26px;border-radius:50%;background:var(--blue)}
.utility{left:474px;top:0;width:415px;height:51px;background:var(--blue);display:flex;align-items:center;padding-left:34px;gap:4px}
.social{width:22px;height:22px;background:var(--white);border-radius:2px}
.search{margin-left:22px;width:248px;height:28px;border:2px solid var(--white);border-radius:8px;color:var(--white);font-size:15px;display:flex;align-items:center;justify-content:space-between;padding:0 12px}
.login{left:896px;top:0;width:215px;height:51px;background:var(--blue-dark);color:var(--white);font-size:16px;display:flex;align-items:center;justify-content:center;gap:8px}
.nav{top:72px;font-size:15px;color:#333}

/* hero */
.hero{left:0;top:117px;width:1200px;height:538px;background:linear-gradient(180deg,#b7aa9b 0%,#8a6e56 45%,#3f342c 100%)}
.hero-quote{left:0;top:506px;width:1200px;text-align:center;color:var(--white);font-weight:600;font-size:40px;line-height:52px;text-shadow:0 2px 6px rgba(0,0,0,.35)}
.hero-arrow{top:320px;width:52px;height:52px;border-radius:50%;background:rgba(255,255,255,.25);display:flex;align-items:center;justify-content:center}

/* campuses */
.map{background:linear-gradient(135deg,#a8dc8c 0%,#dfe6dc 45%,#e7e7e7 100%)}
.accent-rect{background:var(--blue)}
.dot{border-radius:50%;background:#5d98c8}
.campus{background:var(--panel)}
.campus h2{position:absolute;left:149px;top:82px;font-weight:600;font-size:31px;color:var(--blue-dark)}
.campus p{position:absolute;left:149px;top:148px;width:318px;font-size:15.5px;line-height:25.7px;text-align:justify}

/* announcements */
.announce{left:0;top:1564px;width:1200px;height:699px;background:var(--band)}
.announce h2{position:absolute;top:87px;width:1200px;text-align:center;font-weight:600;font-size:32px;color:var(--blue-dark)}
.card{top:190px;width:325px;height:411px;background:var(--white)}
.card-img{position:absolute;left:8px;top:8px;width:309px;height:222px}
.card h3{position:absolute;left:27px;top:260px;font-weight:500;font-size:19px;color:var(--blue-dark)}
.card p{position:absolute;left:28px;top:293px;width:268px;font-size:15.5px;line-height:21px;color:var(--grey-text);text-align:justify}
.card-feature{position:absolute;left:8px;top:8px;width:309px;height:396px;background:var(--blue-mid);color:var(--white);text-align:center}
.card-feature h3{position:static;color:var(--white);font-size:20px;font-weight:600;margin-top:178px}
.card-feature a{display:block;margin:24px auto 0;width:250px;color:var(--white);font-size:15.5px;line-height:26px;text-decoration:underline}
.ann-arrow{top:331px;width:40px;height:40px;border-radius:50%;background:#6b6b6b;display:flex;align-items:center;justify-content:center}

/* quick action circles */
.action{top:2450px;width:222px;height:222px;border-radius:50%;background:var(--blue-dark)}
.action span{position:absolute;left:4px;top:0;width:204px;height:204px;border-radius:50%;background:var(--blue);color:var(--white);font-size:22px;font-weight:500;line-height:33px;display:flex;align-items:center;justify-content:center;text-align:center}

/* footer */
.footer{left:0;top:2764px;width:1200px;height:270px;background:var(--blue-dark);color:var(--white)}
.footer h4{position:absolute;top:64px;font-size:14.5px;font-weight:600}
.footer .col{position:absolute;top:98px;font-size:15.5px;line-height:21px}
.ack{left:94px;width:238px;text-align:justify}
.links{left:399px;list-style:none}
.links li{line-height:26px}
.links li::before{content:"";display:inline-block;width:4px;height:4px;border-radius:50%;background:var(--white);margin:0 10px 3px 4px}
.row{display:flex;gap:10px;align-items:flex-start;margin-bottom:20px}
.bottom{left:0;top:3034px;width:1200px;height:81px;background:var(--blue);color:var(--white);font-size:14px}
</style>
</head>
<body>
<div class="page">

  <!-- header -->
  <div class="abs brand"><span class="brand-dot"></span>BRIMLEY COLLEGE</div>
  <div class="abs utility">
    <span class="social"></span><span class="social"></span><span class="social"></span>
    <div class="search">Search..
      <svg width="16" height="16" viewBox="0 0 16 16"><circle cx="10" cy="6" r="4.5" fill="none" stroke="#fff" stroke-width="1.6"/><path d="M7 9 2 14" stroke="#fff" stroke-width="1.8"/></svg>
    </div>
  </div>
  <div class="abs login">Login
    <svg width="20" height="20" viewBox="0 0 20 20"><circle cx="10" cy="6" r="4.5" fill="none" stroke="#fff" stroke-width="1.5"/><path d="M2 19c1-5 4-7 8-7s7 2 8 7" fill="none" stroke="#fff" stroke-width="1.5"/></svg>
  </div>
  <span class="abs nav" style="left:379px">About Us</span>
  <span class="abs nav" style="left:474px">Learning</span>
  <span class="abs nav" style="left:569px">Student Life</span>
  <span class="abs nav" style="left:683px">Enrolment</span>
  <span class="abs nav" style="left:789px">Community</span>
  <span class="abs nav" style="left:907px">New &amp; Events</span>
  <span class="abs nav" style="left:1034px">Contact Us</span>

  <!-- hero -->
  <div class="abs hero" role="img" aria-label="Photo of uniformed school children running joyfully down a school corridor"></div>
  <div class="abs hero-quote">“EDUCATION IS THE KEY TO UNLOCKING THE WORLD<br>A PASSPORT TO FREEDOM.”</div>
  <div class="abs hero-arrow" style="left:28px"><svg width="22" height="30" viewBox="0 0 22 30"><path d="M17 3 5 15l12 12" fill="none" stroke="#555" stroke-width="2.5"/></svg></div>
  <div class="abs hero-arrow" style="left:1126px"><svg width="22" height="30" viewBox="0 0 22 30"><path d="M5 3l12 12L5 27" fill="none" stroke="#555" stroke-width="2.5"/></svg></div>

  <!-- campus maps -->
  <div class="abs dot" style="left:28px;top:778px;width:25px;height:25px"></div>
  <div class="abs dot" style="left:43px;top:831px;width:33px;height:33px"></div>
  <div class="abs accent-rect" style="left:35px;top:1031px;width:186px;height:100px"></div>
  <div class="abs map" style="left:82px;top:779px;width:453px;height:322px" role="img" aria-label="Street map around the Lynwood campus"></div>

  <div class="abs dot" style="left:1142px;top:778px;width:25px;height:25px"></div>
  <div class="abs dot" style="left:1118px;top:831px;width:33px;height:33px"></div>
  <div class="abs accent-rect" style="left:974px;top:1031px;width:186px;height:100px"></div>
  <div class="abs map" style="left:633px;top:779px;width:481px;height:322px" role="img" aria-label="Street map around the Ferndale campus"></div>

  <div class="abs campus" style="left:0;top:1167px;width:536px;height:322px">
    <h2>LYNWOOD CAMPUS</h2>
    <p>Lorem ipsum dolor sit amet, consectetur adipiscing elit. Maecenas ante turpis, rhoncus ut nunc quis, efficitur blandit massa. Nam volutpat, ante ac ullamco</p>
  </div>
  <div class="abs campus" style="left:634px;top:1167px;width:566px;height:322px">
    <h2 style="left:76px;top:80px">FERNDALE CAMPUS</h2>
    <p style="left:76px;top:146px">Lorem ipsum dolor sit amet, consectetur adipiscing elit. Maecenas ante turpis, rhoncus ut nunc quis, efficitur blandit massa. Nam volutpat, ante ac ullamco</p>
  </div>

  <!-- announcements -->
  <section class="abs announce">
    <h2>ANNOUNCEMENTS</h2>
    <div class="abs ann-arrow" style="left:27px"><svg width="14" height="20" viewBox="0 0 14 20"><path d="M11 2 3 10l8 8" fill="none" stroke="#fff" stroke-width="2"/></svg></div>
    <div class="abs ann-arrow" style="left:1127px"><svg width="14" height="20" viewBox="0 0 14 20"><path d="M3 2l8 8-8 8" fill="none" stroke="#fff" stroke-width="2"/></svg></div>

    <article class="abs card" style="left:85px">
      <div class="card-img" style="background:linear-gradient(160deg,#6f8f78 0%,#c9a77a 60%,#e8d9b8 100%)" role="img" aria-label="Photo of young students reading books on a bench"></div>
      <h3>EVENT 1</h3>
      <p>Nulla ligula justo, imperdiet a interdum in, scelerisque at lectus. Vestibulum velit ipsum, hendrerit eget eros sit amet</p>
    </article>
    <article class="abs card" style="left:437px">
      <div class="card-feature">
        <h3>LOREM IPSUM DOLOR</h3>
        <a>Lorem ipsum dolor sit amet, consectetur adipiscing elit.</a>
      </div>
    </article>
    <article class="abs card" style="left:788px">
      <div class="card-img" style="background:linear-gradient(160deg,#e7e3dc 0%,#c8b29a 55%,#8a7a68 100%)" role="img" aria-label="Photo of students working at desks in a classroom"></div>
      <h3>EVENT3</h3>
      <p>Nulla ligula justo, imperdiet a interdum in, scelerisque at lectus. Vestibulum velit ipsum, hendrerit eget eros sit amet</p>
    </article>
  </section>

  <!-- quick actions -->
  <div class="abs action" style="left:89px"><span>BOOK A<br>TOUR</span></div>
  <div class="abs action" style="left:357px"><span>ENROLMENT<br>APPLICATION<br>FORM</span></div>
  <div class="abs action" style="left:624px"><span>PROSPECTUS</span></div>
  <div class="abs action" style="left:887px"><span>FAQ</span></div>

  <!-- footer -->
  <footer class="abs footer">
    <h4 style="left:94px">ACKNOWLEDGEMENT</h4>
    <h4 style="left:399px">QUICK LINKS</h4>
    <h4 style="left:583px">LOCATION</h4>
    <h4 style="left:862px">CONTACT US</h4>
    <p class="col ack">Lorem ipsum dolor sit amet, consectetur adipiscing elit. Maecenas ante turpis, rhoncus ut nunc quis, efficitur blandit massa. Nam volutpat, ante ac ullamcorper dictum,</p>
    <ul class="col links" style="top:90px">
      <li>About Us</li><li>Learning</li><li>Student Life</li><li>Enrolment</li><li>Commmunity</li>
    </ul>
    <div class="col" style="left:583px;top:96px">
      <div class="row"><svg width="12" height="16" viewBox="0 0 12 16"><path d="M6 0a6 6 0 0 1 6 6c0 4-6 10-6 10S0 10 0 6a6 6 0 0 1 6-6z" fill="#fff"/><circle cx="6" cy="6" r="2.2" fill="#1a66a3"/></svg><span>18 Brellin Rd, Lynwood<br>WA 6147</span></div>
      <div class="row"><svg width="12" height="16" viewBox="0 0 12 16"><path d="M6 0a6 6 0 0 1 6 6c0 4-6 10-6 10S0 10 0 6a6 6 0 0 1 6-6z" fill="#fff"/><circle cx="6" cy="6" r="2.2" fill="#1a66a3"/></svg><span>7 Tamsel Way, Ferndale<br>WA 6148</span></div>
    </div>
    <div class="col" style="left:862px;top:94px">
      <div class="row"><svg width="16" height="16" viewBox="0 0 16 16"><path d="M3 1l3 3-2 2c1 2 3 4 5 5l2-2 3 3-2 3C7 15 1 9 1 3z" fill="#fff"/></svg><span>+61 8 9412 7788</span></div>
      <div class="row" style="margin-top:-4px"><svg width="18" height="14" viewBox="0 0 18 14"><rect x="0.5" y="0.5" width="17" height="13" fill="#fff"/><path d="M1 1l8 7 8-7" fill="none" stroke="#1a66a3" stroke-width="1.3"/></svg><span>admin@brimley-example.edu.au</span></div>
    </div>
  </footer>
  <div class="abs bottom">
    <span class="abs" style="left:88px;top:30px">Copyright © 2023 All Rights Reserved By Brimley College</span>
    <span class="abs" style="left:604px;top:30px">CRICOS Provider Number: 01234X ABN: 12 345 678 901 &nbsp;| Privacy &nbsp;| Disclaimer</span>
  </div>
</div>
</body>
</html>
```